Sprinkles & Tails 2nd Annual Fundraiser

I am a Realtor sponsoring the 2nd annual fundraiser on behalf of Allies of Harlow Vale Animal Haven. Like the flyer to be professional yet fun and inviting. Please see the attached file below. The 1st annual flyer was fun but not as professional, modern or inviting as I would have liked it to be.
Target Market(s)
Dog lovers in Ponte Vedra, Ponte Vedra Beach and Nocatee Florida
Logo Text
Needed
Font styles to use
Other font styles liked:
- Font that fits the style of the fundraiser
Colors
886aae
abd036
Requirements
Must have
- Please see the attached flyer and photos.
- This will be the 2nd Annual on Saturday, April 27, 2019 from 10AM - 1PM. Same location: Kendrick Realty, 418 Tillbrook Ave. Ponte Vedra FL 32075

```html
<!DOCTYPE html>
<html lang="en">
<head>
<meta charset="utf-8">
<title>Sprinkles &amp; Tails – 2nd Annual Fundraiser</title>
<link rel="stylesheet" href="https://fonts.googleapis.com/css2?family=Fredoka:wght@500;700&family=Montserrat:wght@400;600;700;800&display=swap">
<style>
  :root {
    --purple: #886aae;
    --purple-deep: #5e4285;
    --green: #abd036;
    --green-deep: #7f9e1f;
    --ink: #3b2d52;
    --paper: #ffffff;
    --page: #e9e9ec;
    --grey-text: #6b6b72;
  }
  * { box-sizing: border-box; margin: 0; padding: 0; }
  html, body { width: 811px; height: 1200px; overflow: hidden; background: var(--page); }
  body { font-family: "Montserrat", sans-serif; color: var(--ink); }

  .flyer { position: relative; width: 811px; height: 1200px; background: var(--paper); overflow: hidden; }

  /* Header photo area */
  .photo-collage {
    position: absolute; left: 0; top: 0; width: 540px; height: 430px;
    background: linear-gradient(160deg, #b9a48f 0%, #8d7b6e 45%, #c7bfb3 100%);
  }
  .photo-circle {
    position: absolute; border-radius: 50%; border: 5px solid var(--paper);
    background: linear-gradient(135deg, #9a8f86, #d2c6b6);
  }
  .photo-circle.one { left: 395px; top: 40px; width: 120px; height: 120px; }
  .photo-circle.two { left: 420px; top: 175px; width: 105px; height: 105px; background: linear-gradient(135deg, #a6b08f, #7d8670); }
  .photo-circle.three { left: 395px; top: 295px; width: 115px; height: 115px; background: linear-gradient(135deg, #c9b39b, #8e7a66); }

  .support-panel {
    position: absolute; left: 540px; top: 0; width: 271px; height: 430px;
    display: flex; flex-direction: column; align-items: center; padding-top: 48px; text-align: center;
  }
  .support-label { font-family: "Fredoka", sans-serif; font-weight: 700; font-size: 26px; color: var(--purple); letter-spacing: 1px; }
  .partner-name {
    margin-top: 26px; display: flex; flex-direction: column; align-items: center; gap: 12px;
    font-family: "Fredoka", sans-serif; font-weight: 700; font-size: 27px; line-height: 1.15; color: var(--purple-deep);
    padding: 0 20px;
  }
  .partner-name .mark { width: 46px; height: 46px; border-radius: 50%; background: var(--green); }
  .partner-tagline { margin-top: 18px; font-size: 12px; color: var(--grey-text); line-height: 1.4; padding: 0 30px; }

  /* Title */
  .title-block { position: absolute; left: 40px; top: 448px; width: 731px; }
  .edition { font-family: "Fredoka", sans-serif; font-weight: 700; font-size: 30px; color: var(--purple); letter-spacing: 1px; }
  .event-name { font-family: "Fredoka", sans-serif; font-weight: 700; font-size: 64px; line-height: 1; color: var(--purple-deep); letter-spacing: 1px; }
  .event-name .amp { color: var(--green); }
  .event-sub { font-family: "Fredoka", sans-serif; font-weight: 700; font-size: 25px; color: var(--green-deep); letter-spacing: 2px; margin-top: 4px; }

  .tagline-band {
    position: absolute; left: 0; top: 602px; width: 811px; height: 48px;
    background: var(--purple); color: var(--paper);
    font-family: "Fredoka", sans-serif; font-weight: 700; font-size: 25px; letter-spacing: 1px;
    display: flex; align-items: center; padding-left: 40px;
  }
  .tagline-band::after {
    content: ""; position: absolute; right: 0; top: 0; width: 140px; height: 48px; background: var(--green);
    clip-path: polygon(30px 0, 100% 0, 100% 100%, 0 100%);
  }

  /* Details */
  .details { position: absolute; left: 40px; top: 668px; width: 731px; display: flex; justify-content: space-between; }
  .detail-row { font-size: 21px; font-weight: 600; color: var(--ink); margin-bottom: 10px; }
  .detail-label { font-family: "Fredoka", sans-serif; font-weight: 700; font-size: 28px; color: var(--purple); margin-right: 8px; }
  .location { width: 300px; }
  .location .detail-label { display: block; margin-bottom: 4px; }
  .location p { font-size: 16px; font-weight: 600; line-height: 1.35; }

  /* Features */
  .features {
    position: absolute; left: 40px; top: 790px; width: 731px;
    display: grid; grid-template-columns: 1fr 1fr; gap: 8px 14px;
  }
  .feature {
    background: var(--green); color: var(--ink); font-weight: 700; font-size: 16px;
    padding: 9px 14px; display: flex; align-items: center; gap: 10px;
  }
  .feature svg { flex: none; }

  .donate { position: absolute; left: 40px; top: 928px; width: 731px; display: flex; align-items: center; justify-content: space-between; }
  .donate-line { font-size: 15px; font-weight: 600; }
  .donate-line strong { color: var(--purple-deep); }
  .donate-button {
    background: var(--purple); color: var(--paper); font-weight: 800; font-size: 14px;
    padding: 8px 18px; border-radius: 4px; letter-spacing: 1px;
  }
  .fine-print { position: absolute; left: 40px; top: 972px; width: 731px; font-size: 12.5px; line-height: 1.45; color: var(--grey-text); }

  /* Footer */
  .sponsor { position: absolute; left: 40px; top: 1040px; width: 360px; }
  .sponsor-label { font-size: 12px; font-weight: 700; color: var(--purple); letter-spacing: 1px; text-transform: uppercase; }
  .sponsor-name { margin-top: 8px; display: flex; align-items: center; gap: 10px; font-weight: 800; font-size: 22px; color: var(--ink); }
  .sponsor-name .mark { width: 22px; height: 22px; background: var(--green); }
  .sponsor-agent { margin-top: 10px; font-size: 14px; font-weight: 600; line-height: 1.45; }
  .sponsor-agent span { display: block; font-weight: 400; color: var(--grey-text); }

  .footer-photo {
    position: absolute; left: 440px; top: 1020px; width: 371px; height: 180px;
    background: linear-gradient(150deg, #d7c2a0 0%, #b08858 55%, #8f9fb0 100%);
  }
  .footer-bar { position: absolute; left: 0; bottom: 0; width: 440px; height: 14px; background: var(--purple); }
</style>
</head>
<body>
<main class="flyer">
  <div class="photo-collage" role="img" aria-label="Photo of children and adults washing a dog outdoors"></div>
  <div class="photo-circle one" role="img" aria-label="Circular photo of a dog being bathed"></div>
  <div class="photo-circle two" role="img" aria-label="Circular photo of a freshly washed dog"></div>
  <div class="photo-circle three" role="img" aria-label="Circular photo of a volunteer with a dog"></div>

  <aside class="support-panel">
    <div class="support-label">IN SUPPORT OF</div>
    <div class="partner-name"><span class="mark"></span>Allies of Harlow Vale Animal Haven</div>
    <p class="partner-tagline">Helping local pets find loving homes</p>
  </aside>

  <header class="title-block">
    <div class="edition">SECOND ANNUAL</div>
    <h1 class="event-name">SPRINKLES <span class="amp">&amp;</span> TAILS</h1>
    <div class="event-sub">DOGGIE WASH EXTRAVAGANZA</div>
  </header>

  <div class="tagline-band">A FAMILY FUN EVENT FOR ALL AGES</div>

  <section class="details">
    <div class="when">
      <div class="detail-row"><span class="detail-label">Date:</span>Saturday, April 27th, 2019</div>
      <div class="detail-row"><span class="detail-label">Time:</span>10AM – 1PM</div>
    </div>
    <div class="location">
      <span class="detail-label">Location:</span>
      <p>Kendrick Realty, 418 Tillbrook Ave.<br>Ponte Vedra FL 32075</p>
    </div>
  </section>

  <ul class="features">
    <li class="feature"><svg width="16" height="16" viewBox="0 0 16 16"><path d="M2 8l4 4 8-9" fill="none" stroke="#5e4285" stroke-width="2.5"/></svg>FREE Doggie Wash</li>
    <li class="feature"><svg width="16" height="16" viewBox="0 0 16 16"><path d="M2 8l4 4 8-9" fill="none" stroke="#5e4285" stroke-width="2.5"/></svg>Vendors (FREE give a ways)</li>
    <li class="feature"><svg width="16" height="16" viewBox="0 0 16 16"><path d="M2 8l4 4 8-9" fill="none" stroke="#5e4285" stroke-width="2.5"/></svg>Food &amp; Beverages</li>
    <li class="feature"><svg width="16" height="16" viewBox="0 0 16 16"><path d="M2 8l4 4 8-9" fill="none" stroke="#5e4285" stroke-width="2.5"/></svg>Raffle Drawings</li>
    <li class="feature"><svg width="16" height="16" viewBox="0 0 16 16"><path d="M2 8l4 4 8-9" fill="none" stroke="#5e4285" stroke-width="2.5"/></svg>Pet Photos</li>
    <li class="feature"><svg width="16" height="16" viewBox="0 0 16 16"><path d="M2 8l4 4 8-9" fill="none" stroke="#5e4285" stroke-width="2.5"/></svg>Donation Bins</li>
  </ul>

  <div class="donate">
    <p class="donate-line"><strong>To Make a Donation:</strong> www.harlowvalehaven.org/donate</p>
    <span class="donate-button">CLICK DONATE</span>
  </div>
  <p class="fine-print">All donated funds go straight to animal care. Please bring a donation of dog food, toys, towels or blankets for the shelter pets.</p>

  <section class="sponsor">
    <div class="sponsor-label">Sponsored by</div>
    <div class="sponsor-name"><span class="mark"></span>Kendrick Realty</div>
    <p class="sponsor-agent">Dana Whitmore, Realtor<span>418 Tillbrook Ave. Ponte Vedra FL 32075</span></p>
  </section>

  <div class="footer-photo" role="img" aria-label="Photo of the realtor sitting with a golden dog"></div>
  <div class="footer-bar"></div>
</main>
</body>
</html>
```